Lionel Arbusto and Dwight Halvorsen Advertisement

We would like an ad that conveys understated elegance. We are a company that purchases estate jewelry watches and diamonds. We care to a wealthy, upscale clientele.

Target Market(s)

Wealthy upscale.

Industry/Entity Type

It Company

Requirements
Must have
• Elegant Design. Crisp Clean. Attached a doc of how the ad should be arranged.

```html
<!DOCTYPE html>
<html lang="en">
<head>
<meta charset="utf-8">
<title>Lionel Arbusto &amp; Dwight Halvorsen — Ready To Sell?</title>
<link rel="stylesheet" href="https://fonts.googleapis.com/css2?family=Playfair+Display:wght@600;700;800&display=swap">
<style>
  :root {
    --paper: #ffffff;
    --cream: #f7f5e6;
    --cream-soft: #eef0e2;
    --mist: #c9d6d3;
    --slate: #6f8496;
    --navy: #34465c;
    --ink: #1c1a1a;
    --gem-light: #f4f4f4;
    --gem-mid: #b9b9bb;
    --gem-dark: #5d5d60;
  }
  * { margin: 0; padding: 0; box-sizing: border-box; }
  html, body {
    width: 936px;
    height: 1200px;
    overflow: hidden;
    background: var(--paper);
  }
  .ad {
    position: absolute;
    left: 20px;
    top: 20px;
    width: 896px;
    height: 1160px;
    overflow: hidden;
    background:
      radial-gradient(ellipse 70% 48% at 50% 52%, var(--cream) 0%, var(--cream) 55%, rgba(247,245,230,0) 100%),
      linear-gradient(180deg, var(--slate) 0%, var(--mist) 14%, var(--cream-soft) 32%, var(--cream) 50%, var(--cream-soft) 70%, var(--mist) 86%, var(--navy) 100%);
    color: var(--ink);
    text-align: center;
  }
  .headline {
    position: absolute;
    top: 148px;
    left: 0;
    width: 100%;
    font-family: "Playfair Display", Georgia, serif;
    font-weight: 800;
    font-size: 75px;
    letter-spacing: -2.5px;
    line-height: 1;
  }
  .gem-photo {
    position: absolute;
    left: 276px;
    top: 264px;
    width: 320px;
    height: 312px;
  }
  .brand-name {
    position: absolute;
    top: 690px;
    left: 0;
    width: 100%;
    font-family: "Playfair Display", Georgia, serif;
    font-weight: 600;
    font-size: 18px;
    letter-spacing: 0.5px;
    color: var(--ink);
  }
  .promise {
    position: absolute;
    top: 786px;
    left: 0;
    width: 100%;
    font-family: "Playfair Display", Georgia, serif;
    font-weight: 800;
    font-size: 38px;
    letter-spacing: 1.5px;
    line-height: 52px;
  }
  .contact {
    position: absolute;
    top: 940px;
    left: 0;
    width: 100%;
    font-family: "Playfair Display", Georgia, serif;
    font-weight: 600;
    font-size: 20px;
    line-height: 28.7px;
    font-style: normal;
  }
</style>
</head>
<body>
  <main class="ad">
    <h1 class="headline">Ready To Sell?</h1>

    <svg class="gem-photo" viewBox="0 0 320 312" role="img" aria-label="Photograph of a large emerald-cut diamond resting on its corner">
      <defs>
        <linearGradient id="gemTone" x1="0" y1="0" x2="1" y2="1">
          <stop offset="0" stop-color="var(--gem-light)"/>
          <stop offset="0.45" stop-color="var(--gem-mid)"/>
          <stop offset="0.75" stop-color="var(--gem-light)"/>
          <stop offset="1" stop-color="var(--gem-dark)"/>
        </linearGradient>
        <radialGradient id="gemShadow" cx="0.5" cy="0.5" r="0.5">
          <stop offset="0" stop-color="#000" stop-opacity="0.22"/>
          <stop offset="1" stop-color="#000" stop-opacity="0"/>
        </radialGradient>
      </defs>
      <ellipse cx="110" cy="262" rx="100" ry="18" fill="url(#gemShadow)"/>
      <rect x="30" y="16" width="270" height="270" rx="26" fill="url(#gemTone)" transform="rotate(8 165 151)"/>
    </svg>

    <p class="brand-name">Lionel Arbusto &amp; Dwight Halvorsen</p>

    <h2 class="promise">Utmost Discretion<br>By Appointment</h2>

    <address class="contact">
      Via Solana<br>
      318-B Coral Avenue<br>
      Seabright, FL 33491<br>
      support@arbustohalvorsen.com<br>
      561.555.0142
    </address>
  </main>
</body>
</html>
```